Ned the Coach's Tutoring and Test Prep Flyer

We need a flyer that represents our:

AP Level Tutoring
Test Prep (SAT/ACT, etc) Services
Tutoring for ANYONE
Specialty with Learning Disabilities
Anyone, any subject, any test - We can do it!
Free 30 Minute Cognitive Evaluation/Consultation

We want to target as wide of an audience as possible, yet also emphasize the fact that we specialize in tutoring students with learning disabilities.

We are a small, private, tutoring business that is family oriented. We foster successful mentoring and tutoring relationships with our students. We are their advocates in general, not just their tutor.

Target Market(s)

Education
Parents of K-12
College Students
Learning Disability Centers/Specialist

Industry/Entity Type

Tutoring

Colors
9bcb3c

Requirements
Must have
• Address:
• Ned the Coach's Learning Studios
• 4082 Marlow Blvd, Ste. C
• Linden Falls, OR 97321
• Map to show location (not cluttered)
• Contact information
• Professional but still inviting
• Must mention our free 30-minute consultation/cognitive evaluations
Nice to have
• Education/School related decals/arts
• Tutoring graphics
Should not have
• Nothing related to pricing

```html
<!DOCTYPE html>
<html lang="en">
<head>
<meta charset="utf-8">
<title>Ned the Coach's Learning Studios – Tutoring &amp; Test Prep</title>
<link rel="stylesheet" href="https://fonts.googleapis.com/css2?family=Bebas+Neue&family=Lato:wght@400;700&display=swap">
<style>
  :root {
    --brand-green: #9bcb3c;
    --brand-ink: #1f4a26;
    --photo-warm: #b89a7e;
    --photo-dark: #4a3a30;
    --photo-light: #e8e2d6;
    --banner-olive: #a4b544;
    --banner-olive-light: #cfd06a;
    --banner-orange: #c8793f;
    --banner-yellow: #c9c840;
    --banner-brown: #b9773f;
    --banner-salmon: #d9846a;
    --banner-dark: #3a2620;
    --edge-shadow: rgba(0,0,0,0.28);
    --body-text: #2b2b22;
    --white: #ffffff;
    --map-base: #ddd9cf;
  }
  html, body { margin: 0; padding: 0; overflow: hidden; }
  body { width: 848px; height: 1200px; background: var(--white); }
  .flyer { position: relative; width: 848px; height: 1200px; overflow: hidden; font-family: 'Lato', sans-serif; }

  .hero-photo {
    position: absolute; left: 0; top: 0; width: 848px; height: 842px;
    background:
      radial-gradient(ellipse at 78% 8%, rgba(255,255,255,0.75), transparent 45%),
      radial-gradient(ellipse at 20% 55%, rgba(120,80,60,0.55), transparent 50%),
      radial-gradient(ellipse at 85% 60%, rgba(110,30,30,0.55), transparent 45%),
      linear-gradient(180deg, var(--photo-dark) 0%, var(--photo-warm) 45%, var(--photo-light) 100%);
  }

  .offer-stack { position: absolute; left: 212px; top: 82px; width: 428px; }
  .offer {
    position: relative; margin-bottom: 7px; color: var(--white);
    font-family: 'Bebas Neue', sans-serif; text-align: center;
    line-height: 1; box-shadow: inset 7px 0 0 var(--edge-shadow);
  }
  .offer--ap { height: 66px; font-size: 64px; line-height: 70px;
    background: linear-gradient(90deg, var(--banner-olive), var(--banner-olive-light)); }
  .offer--testprep { height: 44px; font-size: 33px; line-height: 48px; background: var(--banner-orange); }
  .offer--anyone { height: 60px; font-size: 56px; line-height: 64px; background: var(--banner-yellow); }
  .offer--specialty { height: 43px; font-size: 31px; line-height: 47px; background: var(--banner-brown); }
  .offer--promise { height: 90px; font-size: 40px; line-height: 42px; letter-spacing: 4px;
    padding-top: 4px; box-sizing: border-box; background: var(--banner-salmon); }
  .offer--free { height: 111px; background: var(--banner-dark); padding-top: 6px; box-sizing: border-box; }
  .offer--free .headline { display: block; font-size: 76px; line-height: 72px; }
  .offer--free .subline { display: block; font-size: 30px; line-height: 28px; }

  .info-band { position: absolute; left: 0; top: 842px; width: 848px; height: 358px; background: var(--brand-green); }

  .brand {
    position: absolute; left: 40px; top: 880px; width: 426px; height: 136px;
    display: flex; align-items: center; gap: 20px;
  }
  .brand-mark { flex: none; width: 44px; height: 44px; background: var(--brand-ink); }
  .brand-name {
    margin: 0; font-family: 'Lato', sans-serif; font-weight: 700;
    font-size: 40px; line-height: 46px; color: var(--brand-ink);
  }

  .about {
    position: absolute; left: 42px; top: 1034px; width: 426px; margin: 0;
    font-size: 15.5px; line-height: 20px; color: var(--body-text); text-align: justify; text-indent: 6px;
  }
  .address {
    position: absolute; left: 42px; top: 1129px; margin: 0; font-style: normal;
    font-size: 15px; line-height: 20px; color: var(--white);
  }

  .location-map { position: absolute; left: 488px; top: 868px; width: 347px; height: 295px; }
</style>
</head>
<body>
<main class="flyer">
  <div class="hero-photo" role="img" aria-label="Photo of a tutor with a notebook working with a student at a classroom table"></div>

  <section class="offer-stack">
    <div class="offer offer--ap">AP Level Tutoring</div>
    <div class="offer offer--testprep">Test Prep (SAT/ACT, etc) Services</div>
    <div class="offer offer--anyone">Tutoring for Anyone</div>
    <div class="offer offer--specialty">Specialty with Learning Disabilities</div>
    <div class="offer offer--promise">Anyone, any subject,<br>any test - we can do it!</div>
    <div class="offer offer--free">
      <span class="headline">Free 30 Minute</span>
      <span class="subline">Cognitive Evaluation/Consultation</span>
    </div>
  </section>

  <section class="info-band"></section>

  <div class="brand">
    <span class="brand-mark"></span>
    <p class="brand-name">Ned the Coach's<br>Learning Studio</p>
  </div>

  <p class="about">We are a small, private, tutoring business that is family oriented. We foster successful mentoring and tutoring relationships with our students. We are their advocates in general, not just their tutor.</p>

  <address class="address">Ned the Coach's Learning Studios | 4082 Marlow Blvd, Ste. C<br>Linden Falls, OR 97321</address>

  <div class="location-map" role="img" aria-label="Street map showing the studio location at 4082 Marlow Blvd">
    <svg width="347" height="295" viewBox="0 0 347 295">
      <rect width="347" height="295" fill="var(--map-base)"/>
    </svg>
  </div>
</main>
</body>
</html>
```